Making 6 Posters and 2 large posters for coffee shop

We are Brindle Mug Depot (similar to a brewhollow), planning to make 3 boards for menu, 3 photos to be printed onto the board, and 2 large posters. (dimensions provided). We believe this is a very simple project with not much additional work required as all pictures have been provided.
We are asking for minimalist design. Very simple. All photos have been provided. 3 of the boards, and 2 for the large posters. The menu has been done but it is in PDF and require recreation (pls make similar design)
The menu board and the 3 other photos are roughly square shape. While dimensions are not provided by our contractors yet, designers can roughly get the dimension from the photos of the boards we are planning to replace.
All these posters will be printed with no frames. So it will look something like those menu board at brewhollow.
Urgently need it in next 24 hours.
Instructions all in PPT attached.
File Link provided:
http://qlinkbox.example/7hT3kWz
Thanks.
---- Edited
For the pictures, we are looking for borders like this if possible (VORN - expensive looking border but platinum white, and dark background.) for the large poster, we liek black themed background with some glow if possible around the cups like the kelvaro logo)
http://www.plumtemplates.example/images/thumbs/Onyx-Slate-psd48213.png
http://www.wirefable-news.example/wp-content/uploads/2013/11/kelvaro-signage.jpg
Target Market(s)
Professionals - Lawyers, Bankers, Brokers
Industry/Entity Type
Coffee Shop

```html
<!DOCTYPE html>
<html lang="en">
<head>
<meta charset="utf-8">
<title>Hot Beverage Menu – Brindle Mug Depot</title>
<link rel="stylesheet" href="https://fonts.googleapis.com/css2?family=Arimo:ital,wght@0,400;0,700;1,700&family=Archivo+Black&family=Stardos+Stencil:wght@700&display=swap">
<style>
  :root {
    --board: #000000;
    --chalk: #ffffff;
  }
  * { box-sizing: border-box; margin: 0; padding: 0; }
  html, body { width: 1200px; height: 1200px; overflow: hidden; background: var(--board); }
  .menu-board {
    position: relative;
    width: 1200px;
    height: 1200px;
    background: var(--board);
    color: var(--chalk);
    font-family: "Arimo", Arial, sans-serif;
    font-weight: 700;
  }
  .rule-pair { position: absolute; }
  .rule-pair span {
    position: absolute; left: 0; right: 0; height: 5px; background: var(--chalk);
  }
  .rule-pair span:first-child { top: 0; }
  .rule-pair span:last-child { top: 15px; }
  .rule-top-left  { left: 36px;  width: 311px; top: 101px; height: 20px; }
  .rule-top-right { left: 865px; width: 295px; top: 101px; height: 20px; }
  .rule-bottom    { left: 36px;  width: 1124px; top: 1108px; height: 20px; }

  .menu-title {
    position: absolute; left: 0; right: 0; top: 72px;
    text-align: center;
    font-family: "Stardos Stencil", "Times New Roman", serif;
    font-weight: 700;
    font-size: 62px;
    line-height: 68px;
    letter-spacing: 2px;
  }

  .row {
    position: absolute; left: 131px; width: 938px;
    height: 26px; line-height: 26px;
    font-size: 20.5px;
  }
  .row .price { position: absolute; top: 0; text-align: right; white-space: nowrap; }
  .price.small  { right: 298px; }
  .price.medium { right: 152px; }
  .price.large  { right: 0; }

  .size-head { font-weight: 400; font-size: 17px; }
  .size-oz { font-size: 14px; }

  .section-heading {
    position: absolute; left: 131px;
    font-family: "Archivo Black", "Arial Black", sans-serif;
    font-size: 31px; line-height: 36px;
  }
  .note {
    position: absolute; left: 131px;
    font-size: 16px; line-height: 20px; font-style: italic;
  }
  .note.plain { font-style: normal; font-weight: 400; }
  .row.sub { font-size: 22px; }
  .row.compact { font-size: 17px; }
  .tea-pot-list {
    position: absolute; top: 954px; left: 131px; width: 800px;
    display: grid; grid-template-columns: 350px 1fr;
    font-size: 17px; line-height: 23px; font-style: italic;
  }
</style>
</head>
<body>
<main class="menu-board">
  <div class="rule-pair rule-top-left"><span></span><span></span></div>
  <h1 class="menu-title">HOT BEVERAGE</h1>
  <div class="rule-pair rule-top-right"><span></span><span></span></div>

  <div class="row size-head" style="top:163px"><span class="price small">Small</span><span class="price medium">Medium</span><span class="price large">Large</span></div>
  <div class="row size-oz" style="top:187px"><span class="price small">8oz</span><span class="price medium">12oz</span><span class="price large">16oz</span></div>

  <h2 class="section-heading" style="top:199px">Hot Coffee</h2>
  <div class="row" style="top:234px"><span class="item">Latte / Flat White /</span><span class="price small">5</span><span class="price medium">5.5</span><span class="price large">6</span></div>
  <div class="row" style="top:263px"><span class="item">Hawaiian Latte</span><span class="price small">5.8</span><span class="price medium">6.3</span><span class="price large">6.8</span></div>
  <div class="row" style="top:292px"><span class="item">Nocciellatte</span><span class="price small">5.5</span><span class="price medium">6</span><span class="price large">6.5</span></div>
  <div class="row" style="top:322px"><span class="item">Specialty Latte</span><span class="price small">5.5</span><span class="price medium">6</span><span class="price large">6.5</span></div>
  <p class="note" style="top:354px">(Hazelnut, Vanilla, Caramel, Honey, Coconut)</p>
  <div class="row" style="top:380px"><span class="item">Mocha / White Mocha</span><span class="price small">5.5</span><span class="price medium">6</span><span class="price large">6.5</span></div>
  <div class="row" style="top:409px"><span class="item">Americano</span><span class="price small">4.5</span><span class="price medium">5</span><span class="price large">5.5</span></div>
  <div class="row" style="top:439px"><span class="item">Macchiato</span><span class="price small">4.5</span></div>
  <div class="row" style="top:468px"><span class="item">Espresso</span><span class="price small">4</span></div>
  <p class="note plain" style="top:498px">Additional shot: $1</p>

  <h2 class="section-heading" style="top:561px">Hot Matcha</h2>
  <div class="row" style="top:596px"><span class="item">Matcha Latte</span><span class="price small">6</span><span class="price medium">6.5</span><span class="price large">7</span></div>

  <h2 class="section-heading" style="top:664px">Hot Chocolate</h2>
  <div class="row" style="top:698px"><span class="item">Nocciella Chocolate</span><span class="price small">6.4</span><span class="price medium">6.9</span><span class="price large">7.4</span></div>

  <h2 class="section-heading" style="top:751px">Hot Brewed Tea by 1869 Skipper</h2>
  <div class="row sub" style="top:788px"><span class="item">Caffeinated Tea</span><span class="price small">4.5</span><span class="price medium">5</span><span class="price large">5.5</span></div>
  <p class="note" style="top:815px">Jasmine Green, Darjeeling, Earl Grey, English Breakfast</p>
  <div class="row sub" style="top:848px"><span class="item">De-Caffeinated Tea</span></div>
  <p class="note" style="top:875px">Chamomile, Peppermint</p>
  <div class="row compact" style="top:901px"><span class="price small">4.5</span><span class="price medium">5</span><span class="price large">5.5</span></div>
  <div class="row sub" style="top:928px"><span class="item">Tea Pot Selection</span><span class="price large">9 per Pot</span></div>
  <div class="tea-pot-list">
    <span>Market Row Breakfast (Black Tea)</span><span>Verdant Mint (Caffeine-Free)</span>
    <span>Ageless Earl Grey (Black Tea)</span><span>Chamomile Calm (Caffeine-Free)</span>
    <span>Twilight Mist (Green Tea)</span><span>Bright Berries (Caffeine-Free)</span>
  </div>

  <div class="rule-pair rule-bottom"><span></span><span></span></div>
</main>
</body>
</html>
```